Business Card Design Project - Industrial Motor Rep

Create a business card that utilizes our existing logo found on our website: www.kestrelfluxsupply.com

We are a Industrial Distributor with a focus on electric motors. We represent several key brands which can be found on our web site. Our customer base includes Consultants, Large End Users (TQ, Lusk Chemical, Brevol) and original equipment manufacturers.

Industry/Entity Type

Business

Requirements
Must have
• Name, Title, Phone, Fax, Cell, Website, Mailing address

```html
<!DOCTYPE html>
<html lang="en">
<head>
<meta charset="utf-8">
<title>Kestrel Flux Supply – Business Card</title>
<link href="https://fonts.googleapis.com/css2?family=Arimo:wght@400;700&family=Tinos:wght@400&display=swap" rel="stylesheet">
<style>
  :root {
    --backdrop: #e6e6e4;
    --card: #ffffff;
    --card-edge: #f1f1f1;
    --brand-blue: #1f5ea8;
    --brand-red: #d5232b;
    --ink: #1c1c1c;
    --muted: #7b7f86;
    --divider: #d6d8dc;
  }
  * { box-sizing: border-box; margin: 0; padding: 0; }
  html, body { width: 1200px; height: 944px; overflow: hidden; }
  body {
    background: var(--backdrop);
    font-family: "Arimo", Arial, sans-serif;
    position: relative;
  }
  .card {
    position: absolute;
    width: 600px;
    height: 343px;
    background: linear-gradient(180deg, var(--card) 0%, var(--card-edge) 100%);
    box-shadow: 0 10px 28px rgba(0,0,0,.22);
    overflow: hidden;
  }
  .card--front { left: 70px; top: 80px; }
  .card--back { left: 530px; top: 490px; }

  /* brand block */
  .brand { position: absolute; }
  .brand__row { display: flex; align-items: center; gap: 12px; }
  .brand__dot { border-radius: 50%; background: var(--brand-red); flex: none; }
  .brand__name {
    font-family: "Arimo", Arial, sans-serif;
    font-weight: 700;
    color: var(--brand-blue);
    line-height: 1.05;
  }
  .brand__tagline { color: var(--muted); font-weight: 400; }

  .card--front .brand { left: 78px; top: 118px; }
  .card--front .brand__dot { width: 26px; height: 26px; }
  .card--front .brand__name { font-size: 36px; }
  .card--front .brand__tagline { font-size: 17px; margin: 8px 0 0 38px; }

  .card--back .brand { left: 34px; top: 112px; width: 210px; }
  .card--back .brand__row { gap: 8px; }
  .card--back .brand__dot { width: 14px; height: 14px; }
  .card--back .brand__name { font-size: 21px; }
  .card--back .brand__tagline { font-size: 11px; margin: 6px 0 0 22px; }

  .divider {
    position: absolute; left: 262px; top: 40px;
    width: 1px; height: 210px; background: var(--divider);
  }

  .contact { position: absolute; left: 290px; top: 50px; color: var(--ink); }
  .contact__name { font-family: "Tinos", "Times New Roman", serif; font-size: 24px; color: var(--brand-red); }
  .contact__title { font-size: 15px; font-weight: 700; color: var(--ink); margin-left: 6px; }
  .contact__group { margin-top: 18px; }
  .contact__line {
    display: flex; align-items: center; gap: 10px;
    font-size: 14.5px; line-height: 19px; letter-spacing: .2px;
  }
  .contact__line--cont { padding-left: 24px; }
  .contact__line svg { width: 14px; height: 14px; flex: none; fill: var(--brand-blue); }

  .stripe-red {
    position: absolute; left: 0; right: 0; bottom: 30px; height: 4px; background: var(--brand-red);
  }
  .stripe-blue {
    position: absolute; left: 0; right: 0; bottom: 0; height: 26px; background: var(--brand-blue);
  }
</style>
</head>
<body>

  <section class="card card--front" aria-label="Business card front">
    <div class="brand">
      <div class="brand__row">
        <span class="brand__dot"></span>
        <span class="brand__name">Kestrel Flux Supply, LLC</span>
      </div>
      <p class="brand__tagline">Manufacturers Representatives</p>
    </div>
  </section>

  <section class="card card--back" aria-label="Business card back">
    <div class="brand">
      <div class="brand__row">
        <span class="brand__dot"></span>
        <span class="brand__name">Kestrel Flux Supply, LLC</span>
      </div>
      <p class="brand__tagline">Manufacturers Representatives</p>
    </div>

    <div class="divider"></div>

    <div class="contact">
      <p><span class="contact__name">Alan Reyes</span><span class="contact__title">director</span></p>

      <div class="contact__group">
        <p class="contact__line">
          <svg viewBox="0 0 16 16" aria-hidden="true"><path d="M8 1 1 8h2v7h4v-4h2v4h4V8h2z"/></svg>
          P.O. Box 427316
        </p>
        <p class="contact__line contact__line--cont">Marlow Creek, WI 53990</p>
      </div>

      <div class="contact__group">
        <p class="contact__line">
          <svg viewBox="0 0 16 16" aria-hidden="true"><path d="M4 1 1.5 3c0 6 5.5 11.5 11.5 11.5L15 12l-3-3-2 1.5C8 9.5 6.5 8 5.5 6L7 4z"/></svg>
          262-555-0148
        </p>
        <p class="contact__line">
          <svg viewBox="0 0 16 16" aria-hidden="true"><path d="M4 1h6l2 2v3H4zM2 7h12v6h-2v2H4v-2H2zm3 4v2h6v-2z"/></svg>
          888-555-0192
        </p>
        <p class="contact__line">
          <svg viewBox="0 0 16 16" aria-hidden="true"><path d="M5 0h6a1 1 0 0 1 1 1v14a1 1 0 0 1-1 1H5a1 1 0 0 1-1-1V1a1 1 0 0 1 1-1zm0 2v10h6V2zm3 11a1 1 0 1 0 0 2 1 1 0 0 0 0-2z"/></svg>
          100-555-0107
        </p>
        <p class="contact__line">
          <svg viewBox="0 0 16 16" aria-hidden="true"><circle cx="8" cy="8" r="7"/></svg>
          www.kestrelfluxsupply.com
        </p>
        <p class="contact__line">
          <svg viewBox="0 0 16 16" aria-hidden="true"><path d="M1 3h14v10H1zm1.5 1.5L8 9l5.5-4.5z"/></svg>
          info@kestrelfluxsupply.com
        </p>
      </div>
    </div>

    <div class="stripe-red"></div>
    <div class="stripe-blue"></div>
  </section>

</body>
</html>
```